Lantern Square, Steady Course. (Website Design)

We are launching a new bipartisan civic movement: Lantern Square. Steady Course.
The mission is this: Americans deserve a government that is legally required to serve them honestly.
We are looking for a world-class website designer capable of creating an emotionally powerful, modern, cinematic landing page experience that feels larger than politics.
This is not a campaign website for a political party or candidate. We are not looking for a red, white, and blue page with stripes, or American flags, or stock footage of smiling people in a voting booth. We are looking for an emotional and cinematic experience through and through.
The visual direction should feel:
Historic
Hopeful
American
Emotional
Cinematic
Trustworthy
Timeless
The goal is to make visitors feel that they are witnessing the beginning of something important and want to be part of it in the end.
Primary Objective:
Inspire visitors to participate in a one-minute survey and cast their vote.
The survey itself is extremely short and takes approximately one minute to complete.
Everything on the page should ultimately guide visitors toward this action while creating enough curiosity, trust, emotional engagement, and excitement that they feel compelled to take part in the movement.
Audience:
The audience is ordinary Americans across the political spectrum: Democrats, Republicans, Independents.
The design should feel unifying and welcoming.
It should avoid looking partisan, ideological, activist, or government-issued.
Creative Freedom:
We are intentionally giving designers substantial creative freedom.
We are not looking for someone to simply arrange content into predefined sections.
Instead, we are looking for a designer who can think strategically about user experience and persuasion.
The ideal design is as minimal as possible, but you may always:
Use as many sections as you believe are necessary.
Use as many images as you believe are necessary.
Include storytelling elements.
Include data visualizations.
Include timelines.
Include videos.
Include animations.
Include or exclude sections as you see fit.
Reorganize the flow entirely.
We uploaded some files containing text and section suggestions. You don’t have to use them.
We also uploaded some images to convey the general feel we’re looking for.
We are much more interested in the effectiveness of the overall experience than in any specific layout.
What success looks like:
Think outside the box.
Please do not create another generic political website. We have already explored those approaches.
We are looking for something different.
The winning design will be the one that most effectively guides visitors from curiosity to belief to participation.
When a visitor reaches the end of the experience, they should feel:
This is bigger than politics.
This is something I can support regardless of party.
This feels credible.
This feels hopeful.
I want to be part of this.
Use the survey results, the research findings, the principles, the storytelling, or any other elements you believe will help build trust and inspire participation.
Don't just impress us with flashy visuals. Impress us with a website experience that inspires people to become part of the movement and cast their vote.
The final call-to-action should feel like the natural conclusion of the journey, not a request for engagement.
Our goal is not simply to inform visitors. Our goal is to inspire them to cast their vote.
Prioritize emotional impact, storytelling, clarity, and persuasion over decorative design elements.
Final words:
Design a website experience that successfully inspires visitors to take the survey and cast their vote.
Think like a storyteller, not just a designer.
Thank you for your interest in the project.
Best of luck.

```html
<!DOCTYPE html>
<html lang="en">
<head>
<meta charset="utf-8">
<title>Lantern Square, Steady Course.</title>
<link rel="stylesheet" href="https://fonts.googleapis.com/css2?family=Cormorant+Garamond:wght@500;600&family=Poppins:wght@400;500;600&display=swap">
<style>
:root{
  --navy:#0b1220;
  --navy-2:#0e1627;
  --gold:#a9804f;
  --gold-light:#c29a66;
  --btn:#a98354;
  --red:#a3343c;
  --slate:#67686c;
  --white:#ffffff;
  --ink:#2a2a2a;
  --muted:#6f6f6f;
}
*{margin:0;padding:0;box-sizing:border-box}
html,body{width:1200px;height:3806px;overflow:hidden;background:var(--navy)}
body{position:relative;font-family:"Poppins",sans-serif;color:var(--white)}
.serif{font-family:"Cormorant Garamond",serif;font-weight:600}
.abs{position:absolute}
.center{left:0;width:1200px;text-align:center}
.gold{color:var(--gold)}
.btn{position:absolute;display:flex;align-items:center;justify-content:center;background:var(--btn);color:var(--white);font-size:11.5px;font-weight:600;letter-spacing:.4px;text-transform:uppercase;border-radius:5px}
.section{position:absolute;left:0;width:1200px;overflow:hidden}

/* hero */
.hero{top:0;height:628px;background:
  radial-gradient(ellipse at 78% 40%,rgba(160,70,60,.55),transparent 55%),
  radial-gradient(ellipse at 12% 55%,rgba(150,110,70,.6),transparent 50%),
  linear-gradient(180deg,#3a3a3f 0%,#4a3b33 45%,#3b2a26 100%)}
.nav a{position:absolute;top:30px;font-size:13.5px;color:var(--white);text-decoration:none}
.logo-name{left:161px;top:18px;font-size:22px;line-height:1}
.logo-sub{left:169px;top:41px;font-size:17px;line-height:1;color:var(--gold)}

/* mission */
.mission{top:628px;height:394px;background:var(--navy)}
.photo{position:absolute;background:linear-gradient(160deg,#5a4a3a,#2a241f)}
.journey-date{position:absolute;width:222px;text-align:center;font-size:15px;color:var(--gold);top:1730px}
.journey-text{position:absolute;width:222px;text-align:center;font-size:13.5px;line-height:17px;top:1760px}

/* principles */
.principles{top:2032px;height:588px;background:
  radial-gradient(ellipse at 68% 68%,rgba(210,140,70,.55),transparent 40%),
  linear-gradient(180deg,#1b2130 0%,#2b2b33 55%,#1d1a1c 100%)}
.p-num{position:absolute;left:162px;width:22px;height:22px;border-radius:50%;background:var(--gold);color:var(--navy);font-family:"Cormorant Garamond",serif;font-weight:600;font-size:15px;display:flex;align-items:center;justify-content:center}
.p-text{position:absolute;left:202px;font-size:15px;line-height:18px}
.p-text span{display:block;color:var(--gold)}

/* survey */
.survey{top:2620px;height:691px;background:var(--white);color:var(--ink)}
.card{position:absolute;top:170px;width:172px;height:244px;border-radius:4px;text-align:center;color:var(--white)}
.card .num{position:absolute;top:94px;left:0;width:100%;font-family:"Cormorant Garamond",serif;font-weight:600;font-size:44px}
.card .rule{position:absolute;top:161px;left:16px;right:16px;height:1px;background:rgba(255,255,255,.5)}
.card .label{position:absolute;top:178px;left:0;width:100%;font-size:15px;line-height:18px}
.card svg{position:absolute;left:60px;top:22px}
.stat-num{position:absolute;top:3180px;width:200px;text-align:center;font-size:60px;color:var(--gold);line-height:1}
.stat-label{position:absolute;top:3243px;width:200px;text-align:center;font-size:20px;color:var(--ink)}

/* cta */
.cta{top:3311px;height:495px;background:
  radial-gradient(ellipse at 80% 30%,rgba(90,85,80,.6),transparent 55%),
  linear-gradient(180deg,#23252b 0%,#1d1f25 60%,#141519 100%)}
.footer a{position:absolute;top:3772px;font-size:14px;color:var(--white);text-decoration:none}
.social{position:absolute;top:3773px;width:14px;height:14px;border:1.5px solid var(--white);border-radius:50%}
</style>
</head>
<body>

<!-- HERO -->
<div class="section hero" role="img" aria-label="Sepia monument sculpture and a person holding a waving flag at sunset"></div>
<div class="abs serif logo-name">LANTERN SQUARE</div>
<svg class="abs" style="left:168px;top:47px" width="200" height="4"><line x1="0" y1="2" x2="34" y2="2" stroke="#a9804f"/><line x1="158" y1="2" x2="196" y2="2" stroke="#a9804f"/></svg>
<div class="abs serif logo-sub" style="left:212px">STEADY COURSE</div>
<nav class="nav">
  <a style="left:446px">Our Mission</a>
  <a style="left:560px">The Principles</a>
  <a style="left:687px">The Survey</a>
  <a style="left:797px">Our Journey</a>
</nav>
<div class="btn" style="left:922px;top:19px;width:116px;height:42px;font-size:12px">Vote Now</div>

<div class="abs center serif" style="top:212px;font-size:66px;line-height:76px">A GOVERNMENT</div>
<div class="abs center serif gold" style="top:280px;font-size:38px;line-height:44px;color:var(--gold-light)">THAT IS LEGALLY REQUIRED</div>
<div class="abs center serif" style="top:328px;font-size:23px">TO SERVE THE PEOPLE HONESTLY</div>
<div class="btn" style="left:498px;top:374px;width:206px;height:40px">Take the 1-minute survey</div>
<svg class="abs" style="left:527px;top:441px" width="28" height="28"><circle cx="14" cy="14" r="14" fill="#e8e2d8"/><path d="M11 9l8 5-8 5z" fill="#3a3030"/></svg>
<div class="abs" style="left:566px;top:447px;font-size:12px;font-weight:600;letter-spacing:.4px">WATCH THE VIDEO</div>

<!-- MISSION -->
<div class="section mission"></div>
<div class="abs center serif gold" style="top:694px;font-size:31px">MISSION STATEMENT</div>
<div class="abs center serif" style="top:736px;font-size:37px;line-height:46px;font-weight:500">Today, not a single law binds our government<br>to act honestly, and in our best interest.</div>
<svg class="abs" style="left:437px;top:845px" width="326" height="28"><line x1="0" y1="14" x2="133" y2="14" stroke="#a9804f"/><line x1="193" y1="14" x2="326" y2="14" stroke="#a9804f"/><path d="M163 2l3.5 8h8.5l-7 5 2.7 8.5-7.7-5.3-7.7 5.3 2.7-8.5-7-5h8.5z" fill="#a9804f"/></svg>
<div class="abs center" style="top:890px;font-size:15px;line-height:18px">If our government exists solely to serve us, Why isn’t it<br>legally required to?</div>
<div class="abs center gold" style="top:944px;font-size:14px">We founded this movement to change that.</div>

<!-- WHO WE ARE -->
<div class="abs serif gold" style="left:161px;top:1120px;font-size:31px">WHO WE ARE</div>
<div class="abs serif" style="left:161px;top:1164px;font-size:22px;line-height:27px;width:300px;font-weight:500">We are a bipartisan movement based in Washington, D.C.</div>
<div class="abs" style="left:161px;top:1232px;width:265px;font-size:15px;line-height:17.5px">We believe Americans deserve a government legally required to act honestly, transparently, and in the public’s best interest.</div>
<div class="abs" style="left:161px;top:1321px;width:275px;font-size:15px;line-height:17.5px">At a time of growing division and distrust, we are working to unite Americans around a simple idea: government should faithfully serve the people, not special interests.</div>
<div class="photo" style="left:490px;top:1039px;width:233px;height:228px" role="img" aria-label="Black and white portrait of a civil rights speaker"></div>
<div class="photo" style="left:739px;top:1039px;width:248px;height:228px;background:linear-gradient(160deg,#b08a45,#5a3a20)" role="img" aria-label="Warm-toned portrait of a civil rights leader"></div>
<div class="photo" style="left:1004px;top:1039px;width:196px;height:228px;background:linear-gradient(160deg,#8a8a8a,#3a3a3a)" role="img" aria-label="Black and white portrait of a smiling activist"></div>
<div class="photo" style="left:490px;top:1279px;width:219px;height:226px;background:linear-gradient(180deg,#9a9a98,#4a4a48)" role="img" aria-label="Capitol dome with demonstrators in front"></div>
<div class="photo" style="left:724px;top:1279px;width:257px;height:226px;background:linear-gradient(180deg,#6e6e6e,#2e2e2e)" role="img" aria-label="Speaker waving to a large crowd at a march"></div>
<div class="photo" style="left:996px;top:1279px;width:204px;height:226px;background:linear-gradient(180deg,#7a6a5a,#8a3a34)" role="img" aria-label="Marchers carrying a large protest banner"></div>

<!-- JOURNEY -->
<div class="abs center serif gold" style="top:1572px;font-size:31px">OUR JOURNEY</div>
<svg class="abs" style="left:0;top:1655px" width="1200" height="70" fill="none" stroke="#a9804f" stroke-width="1.5">
  <line x1="268" y1="34" x2="424" y2="34" stroke-width="1"/><circle cx="346" cy="34" r="3.5" fill="#a9804f" stroke="none"/>
  <line x1="522" y1="34" x2="675" y2="34" stroke-width="1"/><circle cx="599" cy="34" r="3.5" fill="#a9804f" stroke="none"/>
  <line x1="773" y1="34" x2="928" y2="34" stroke-width="1"/><circle cx="851" cy="34" r="3.5" fill="#a9804f" stroke="none"/>
  <circle cx="219" cy="34" r="29"/><circle cx="473" cy="34" r="29"/><circle cx="724" cy="34" r="29"/><circle cx="977" cy="34" r="29"/>
  <path d="M210 48V21M210 22h18l-4 6 4 6h-18"/>
  <path d="M465 21h12l5 5v17h-17zM469 31h9M469 35h9M469 39h6"/>
  <path d="M712 27l12-7 12 7zM714 29h20M717 31v10M722 31v10M727 31v10M732 31v10M712 43h24"/>
  <circle cx="970" cy="29" r="3.5"/><circle cx="984" cy="29" r="3.5"/><circle cx="977" cy="27" r="3.5"/><path d="M963 43c0-5 3-8 7-8s7 3 7 8M977 43c0-5 3-8 7-8s7 3 7 8M970 41c0-5 3-9 7-9s7 4 7 9"/>
</svg>
<div class="journey-date" style="left:108px">AUGUST 2024</div>
<div class="journey-date" style="left:362px">OCTOBER 2025</div>
<div class="journey-date" style="left:613px">MARCH 2026</div>
<div class="journey-date" style="left:866px">APRIL 2026</div>
<div class="journey-text" style="left:108px">We started a nonprofit with this goal in mind: Americans deserve an honest government.</div>
<div class="journey-text" style="left:362px">We identified 10 principles that most of Americans agree our government must uphold.</div>
<div class="journey-text" style="left:613px">We turned those principles into a rigorous framework and named it Lantern Square, Steady Course.</div>
<div class="journey-text" style="left:866px">We tested the framework in a pre-registered national study with Americans across the political spectrum.</div>
<svg class="abs" style="left:575px;top:1870px" width="50" height="48"><path d="M25 3l6 15h16l-13 10 5 16-14-10-14 10 5-16-13-10h16z" fill="none" stroke="#a9804f" stroke-width="2"/></svg>
<div class="abs center serif gold" style="top:1936px;font-size:23px">AND THE RESULTS EXCEEDED ALL OUR EXPECTATION</div>

<!-- PRINCIPLES -->
<div class="section principles" role="img" aria-label="Crowd watching sunset over the reflecting pool and monument"></div>
<div class="abs serif gold" style="left:161px;top:2100px;font-size:31px">THE SEVEN PRINCIPLES</div>
<div class="p-num" style="top:2167px">1</div><div class="p-text" style="top:2163px">Public officials should only serve the public good.<span>Not private interests.</span></div>
<div class="p-num" style="top:2225px">2</div><div class="p-text" style="top:2221px">Major governmen truth, and rigorous evidence.<span>Not party loyalty, pressure, or donors.</span></div>
<div class="p-num" style="top:2281px">3</div><div class="p-text" style="top:2277px">When a public decision able to see the reasoning.<span>Clearly. Honestly. On the record.</span></div>
<div class="p-num" style="top:2339px">4</div><div class="p-text" style="top:2335px">And if the flawed, citizens should have a way to challenge it,<span>And get a real response.</span></div>
<div class="p-num" style="top:2397px">5</div><div class="p-text" style="top:2393px">Conflicts of interest in public office all should be disclosed,<span>Before decisions are made.</span></div>
<div class="p-num" style="top:2454px">6</div><div class="p-text" style="top:2450px">Lying or misleading the public in official carry consequences.<span>Real ones.</span></div>
<div class="p-num" style="top:2510px">7</div><div class="p-text" style="top:2506px">And most importantly, Money should never outweigh<br>people’s voice.</div>
<svg class="abs" style="left:771px;top:2186px" width="278" height="278"><circle cx="139" cy="139" r="134" fill="rgba(16,22,36,.78)" stroke="#a9804f" stroke-width="9"/></svg>
<div class="abs serif" style="left:771px;top:2252px;width:278px;text-align:center;font-size:66px;line-height:1;color:var(--gold-light)">89.9%</div>
<div class="abs serif" style="left:771px;top:2330px;width:278px;text-align:center;font-size:23px">SAID</div>
<div class="abs serif" style="left:771px;top:2350px;width:278px;text-align:center;font-size:42px">AGREE</div>

<!-- SURVEY -->
<div class="section survey">
  <div class="abs" style="left:377px;top:62px;width:1px;height:400px;background:#d9d2c8"></div>
  <div class="abs serif gold" style="left:59px;top:84px;font-size:33px">THE SURVEY</div>
  <div class="abs serif gold" style="left:56px;top:122px;font-size:98px;line-height:1">82.9%</div>
  <div class="abs serif" style="left:59px;top:243px;font-size:21px;line-height:23px;color:var(--ink)">OF AMERICANS SAID YES ON<br>A STATE BALLOT VOTE.</div>
  <div class="abs" style="left:59px;top:312px;width:290px;font-size:13.5px;line-height:16px;color:var(--muted)">We conducted a pre-registered national study with X number Americans across the political spectrum.</div>
  <div class="abs" style="left:59px;top:388px;width:206px;height:40px;border:1.5px solid var(--gold);border-radius:4px;color:var(--gold);font-size:11px;font-weight:500;display:flex;align-items:center;justify-content:center">SEE HOW WE DID IT</div>
  <div class="abs" style="left:411px;top:103px;font-size:16px;line-height:20px;color:var(--ink)">We first laid out the 7 principles.<br>We asked if they agree?</div>

  <div class="card" style="left:411px;border:1.5px solid var(--gold);color:var(--ink)">
    <svg width="52" height="52"><circle cx="26" cy="26" r="24" fill="none" stroke="#a9804f" stroke-width="1.5"/><path d="M16 26l7 7 13-14" fill="none" stroke="#a9804f" stroke-width="2"/></svg>
    <div class="num">82.9%</div><div class="rule" style="background:#d8c7b2"></div><div class="label">Said they<br>Agree</div>
  </div>
  <div class="card" style="left:599px;background:var(--gold)">
    <svg width="52" height="52"><circle cx="26" cy="26" r="24" fill="none" stroke="#fff" stroke-width="1.5"/><line x1="16" y1="26" x2="36" y2="26" stroke="#fff" stroke-width="2"/></svg>
    <div class="num">14.4%</div><div class="rule"></div><div class="label">Remained<br>Neutral</div>
  </div>
  <div class="card" style="left:785px;background:var(--red)">
    <svg width="52" height="52"><circle cx="26" cy="26" r="24" fill="none" stroke="#fff" stroke-width="1.5"/><line x1="16" y1="26" x2="36" y2="26" stroke="#fff" stroke-width="2"/></svg>
    <div class="num">2.7%</div><div class="rule"></div><div class="label">Actively<br>Opposed it</div>
  </div>
  <div class="card" style="left:971px;background:var(--slate);text-align:left">
    <svg style="left:14px;top:24px" width="36" height="26" fill="none" stroke="#fff" stroke-width="1.4"><circle cx="10" cy="8" r="4"/><circle cx="26" cy="8" r="4"/><circle cx="18" cy="6" r="4"/><path d="M2 24c0-6 4-9 8-9s8 3 8 9M18 24c0-6 4-9 8-9s8 3 8 9M10 22c0-6 4-10 8-10s8 4 8 10"/></svg>
    <div class="abs" style="left:14px;top:76px;width:150px;font-size:13.5px;line-height:16px">We showed participants the full framework.</div>
    <div class="abs" style="left:14px;top:124px;width:150px;font-size:13.5px;line-height:16px">The legal structure.<br>The enforcement model.<br>The actual mechanism.</div>
  </div>
  <div class="abs" style="left:161px;top:523px;width:878px;height:1px;background:#e4ddd3"></div>
</div>
<div class="stat-num serif" style="left:136px">84.5%</div><div class="stat-label" style="left:136px">DEMOCRATS</div>
<div class="stat-num serif" style="left:382px">80.2%</div><div class="stat-label" style="left:382px">REPUBLICANS</div>
<div class="stat-num serif" style="left:626px">79.9%</div><div class="stat-label" style="left:626px">INDEPENDANTS</div>
<div class="abs" style="left:871px;top:3180px;width:200px;text-align:center;font-size:20px;color:var(--ink)">THEY ALL SAID</div>
<div class="abs serif" style="left:871px;top:3208px;width:200px;text-align:center;font-size:64px;line-height:1;color:var(--gold)">YES</div>

<!-- CTA -->
<div class="section cta" role="img" aria-label="Dusk view of a columned memorial with people gathered in front"></div>
<div class="abs center serif" style="top:3384px;font-size:58px">BE PART OF HISTORY</div>
<div class="abs center serif" style="top:3456px;font-size:29px;color:var(--gold-light)">YOUR VOICE. YOUR VOTE. OUR FUTURE</div>
<div class="btn" style="left:498px;top:3520px;width:206px;height:41px">Take the 1-minute survey</div>
<div class="abs" style="left:400px;top:3615px;width:400px;height:78px;border:1.5px solid rgba(255,255,255,.85);border-radius:8px"></div>
<div class="abs serif" style="left:444px;top:3622px;font-size:54px;line-height:64px">1016</div>
<div class="abs" style="left:559px;top:3636px;font-size:14px;line-height:17px">PEOPLE ALREADY VOTED YES<br>FOR THE BALLOT</div>
<div class="abs" style="left:161px;top:3752px;width:878px;height:1px;background:rgba(255,255,255,.2)"></div>
<footer class="footer">
  <a style="left:161px">About Us</a>
  <a style="left:251px">FAQ</a>
  <a style="left:306px">Privacy Policy</a>
  <a style="left:425px">Contact</a>
</footer>
<div class="social" style="left:945px"></div>
<div class="social" style="left:983px"></div>
<div class="social" style="left:1023px"></div>

</body>
</html>
```